Harcourt Meat Co. Card Design

Industry/Entity Type

Business

Contact Information for Business Card

Front
47b fernhill road Brambleford vic 3971, Greg Harcourt ph 0352918406 mobile 0400583916,

Back
Local quality black angus
Home deliveries
Bulk pack specials
Wholesale available
Private animals cut and packed

Requirements
Must have
• Bullshead to be metallic silver colour like the silver on 1 of the pictured business cards

Flatblack back ground as seen on both business card pictures

Looking alot like the 2 pictured cards nice and neat

```html
<!DOCTYPE html>
<html lang="en">
<head>
<meta charset="utf-8">
<title>Harcourt Meat Co. – Business Card</title>
<link rel="stylesheet" href="https://fonts.googleapis.com/css2?family=Montserrat:wght@400;500&display=swap">
<style>
  :root {
    --page: #e9e7e4;
    --card: #0c0c0d;
    --card-glow: #26272a;
    --silver: #d9d9db;
    --silver-dim: #b7b7ba;
    --red: #e0181f;
    --text: #e6e6e6;
    --muted: #a9a9ab;
  }
  * { box-sizing: border-box; margin: 0; padding: 0; }
  html, body { width: 1200px; height: 900px; overflow: hidden; }
  body {
    background: var(--page);
    font-family: "Montserrat", Arial, sans-serif;
    display: flex;
    align-items: center;
    justify-content: center;
    gap: 60px;
  }
  .card {
    position: relative;
    width: 525px;
    height: 300px;
    background: var(--card);
    overflow: hidden;
    box-shadow: 0 10px 30px rgba(0,0,0,.25);
  }
  .card__texture {
    position: absolute;
    inset: 0;
    background: radial-gradient(ellipse at 60% 40%, var(--card-glow) 0%, var(--card) 70%);
  }
  .brand {
    position: relative;
    display: flex;
    align-items: center;
    gap: 10px;
    color: var(--silver);
    font-weight: 500;
    letter-spacing: .04em;
    white-space: nowrap;
  }
  .brand__dot {
    border-radius: 50%;
    background: var(--silver-dim);
    flex: none;
  }
  /* Front: contact side */
  .card--front .brand { position: absolute; left: 28px; top: 24px; font-size: 15px; }
  .card--front .brand__dot { width: 24px; height: 24px; }
  .contact-list {
    position: absolute;
    left: 28px;
    top: 72px;
    list-style: none;
    display: flex;
    flex-direction: column;
    gap: 8px;
    color: var(--text);
    font-size: 13px;
  }
  .contact-list li { display: flex; align-items: center; gap: 10px; line-height: 1.3; }
  .contact-list .number { font-size: 16px; letter-spacing: .03em; }
  .contact-list .number--mobile { padding-left: 30px; }
  .contact-list .address { align-items: flex-start; }
  .icon { width: 20px; height: 20px; flex: none; }
  .services {
    position: absolute;
    left: 28px;
    bottom: 22px;
    width: 250px;
    color: var(--muted);
    font-size: 10.5px;
    line-height: 1.45;
  }
  .accent-line {
    position: absolute;
    top: 0;
    right: 34px;
    width: 3px;
    height: 100%;
    background: var(--red);
  }
  .accent-corner {
    position: absolute;
    right: 6px;
    bottom: 6px;
  }
  /* Back: brand side */
  .card--back .brand {
    position: absolute;
    left: 50%;
    top: 50%;
    transform: translate(-50%, -50%);
    font-size: 24px;
    gap: 14px;
  }
  .card--back .brand__dot { width: 34px; height: 34px; }
  .card--back .accent-base {
    position: absolute;
    left: 0;
    right: 0;
    bottom: 14px;
    height: 2px;
    background: var(--red);
  }
</style>
</head>
<body>

  <section class="card card--front" aria-label="Business card front">
    <div class="card__texture" role="img" aria-label="Dark hexagonal mesh texture"></div>

    <div class="brand"><span class="brand__dot"></span>Harcourt Meat Co.</div>

    <ul class="contact-list">
      <li class="number number--mobile">0400583916</li>
      <li class="number">
        <svg class="icon" viewBox="0 0 20 20" aria-hidden="true">
          <circle cx="10" cy="10" r="8.5" fill="none" stroke="var(--red)" stroke-width="1.5"/>
          <path d="M7 5.5c-.8.5-1.4 1.3-1 2.6.7 2.5 2.8 4.8 5.3 5.9 1.3.5 2.2 0 2.8-.8l-1.7-1.6-1.2.7c-1.2-.6-2.2-1.7-2.8-2.9l.8-1.1z" fill="var(--text)"/>
        </svg>
        <span>0352918406</span>
      </li>
      <li class="address">
        <svg class="icon" viewBox="0 0 20 20" aria-hidden="true">
          <circle cx="10" cy="10" r="8.5" fill="none" stroke="var(--red)" stroke-width="1.5"/>
          <path d="M7 5.5c-.8.5-1.4 1.3-1 2.6.7 2.5 2.8 4.8 5.3 5.9 1.3.5 2.2 0 2.8-.8l-1.7-1.6-1.2.7c-1.2-.6-2.2-1.7-2.8-2.9l.8-1.1z" fill="var(--text)"/>
        </svg>
        <span>Front 47b fernhill road<br>Brambleford vic 3971</span>
      </li>
      <li>
        <svg class="icon" viewBox="0 0 20 20" aria-hidden="true">
          <circle cx="10" cy="10" r="8.5" fill="none" stroke="var(--red)" stroke-width="1.5"/>
          <path d="M10 5l5 4.5h-1.5V14h-2.5v-3H9v3H6.5V9.5H5z" fill="var(--text)"/>
        </svg>
        <span>Greg Harcourt</span>
      </li>
    </ul>

    <p class="services">*Back Local quality black angus Home deliveries Bulk pack specials Wholesale available Private animals cut and packed</p>

    <div class="accent-line"></div>
    <svg class="accent-corner" width="16" height="16" viewBox="0 0 16 16" aria-hidden="true">
      <polygon points="16,0 16,16 0,16" fill="var(--red)"/>
    </svg>
  </section>

  <section class="card card--back" aria-label="Business card back">
    <div class="card__texture" role="img" aria-label="Dark hexagonal mesh texture"></div>
    <div class="brand"><span class="brand__dot"></span>Harcourt Meat Co.</div>
    <div class="accent-base"></div>
  </section>

</body>
</html>
```